Certificate of Completion - Educational Trainings

We are looking for a certificate of completion for individuals who complete one of our specific trainings. Files should be provided in a Word (docx) or PowerPoint (pptx) format. The "Halvorcrest example.png" file is to show necessary information. Copies of logos have been included for design purposes.

Target Market(s)

Training Participants

Industry/Entity Type

Healthcare

Font styles to use
Sans Serif

```html
<!DOCTYPE html>
<html lang="en">
<head>
<meta charset="utf-8">
<title>Halvorcrest Certificate of Completion</title>
<link rel="stylesheet" href="https://fonts.googleapis.com/css2?family=UnifrakturMaguntia&family=Nunito+Sans:wght@400;700;800&family=Kaushan+Script&family=Mrs+Saint+Delafield&display=swap">
<style>
  :root {
    --page-bg: #e9e9e9;
    --forest: #0f6a28;
    --leaf: #6ab04c;
    --leaf-light: #8cc873;
    --paper: #ffffff;
    --ink: #111111;
    --rule-blue: #7aa6d8;
    --teal-rule: #6fb9b8;
    --grey-rule: #9a9a9a;
  }
  * { box-sizing: border-box; margin: 0; padding: 0; }
  html, body { width: 845px; height: 1200px; overflow: hidden; }
  body { background: var(--page-bg); font-family: "Nunito Sans", Arial, sans-serif; color: var(--ink); position: relative; }

  .certificate {
    position: absolute; left: 32px; top: 322px; width: 780px; height: 555px;
    background: var(--forest);
  }
  .ornament-band {
    position: absolute; left: 18px; top: 18px; right: 18px; bottom: 18px;
    background: repeating-linear-gradient(45deg, var(--leaf) 0 4px, var(--leaf-light) 4px 8px);
  }
  .paper {
    position: absolute; left: 43px; top: 43px; right: 43px; bottom: 43px;
    background: radial-gradient(ellipse at 40% 60%, #ffffff 40%, #eef5f8 100%);
    border: 1px solid var(--rule-blue);
    outline: 3px solid var(--paper);
  }
  .content { position: absolute; left: 0; top: 0; width: 780px; height: 555px; }

  .brand {
    position: absolute; left: 100px; top: 66px; display: flex; align-items: center; gap: 8px;
    font-weight: 800; font-size: 22px; letter-spacing: 1.5px; text-transform: uppercase; color: var(--ink);
  }
  .brand-dot { width: 24px; height: 24px; border-radius: 50%; background: var(--forest); }
  .brand-divider { position: absolute; left: 392px; top: 68px; width: 1px; height: 36px; background: var(--grey-rule); }
  .sponsor-info { position: absolute; left: 405px; top: 71px; font-size: 10.5px; line-height: 14px; text-transform: uppercase; }
  .sponsor-info .registry { color: var(--forest); }

  .title {
    position: absolute; left: 0; width: 780px; top: 104px; text-align: center;
    font-family: "UnifrakturMaguntia", serif; font-size: 108px; line-height: 120px; color: var(--forest);
  }
  .subtitle-row { position: absolute; left: 218px; top: 236px; width: 344px; height: 24px; }
  .subtitle-row .rule { position: absolute; top: 12px; width: 74px; height: 1px; background: var(--teal-rule); }
  .subtitle-row .rule.left { left: 0; } .subtitle-row .rule.right { right: 0; }
  .subtitle-row .cap { position: absolute; top: 5px; width: 14px; height: 14px; border-radius: 7px; background: var(--ink); }
  .subtitle-row .cap.left { left: 80px; } .subtitle-row .cap.right { right: 80px; }
  .pill {
    position: absolute; left: 90px; top: 1px; width: 164px; height: 23px; border-radius: 12px;
    background: var(--leaf); color: #fff; font-size: 15px; line-height: 23px; text-align: center;
  }
  .awarded { position: absolute; left: 0; width: 780px; top: 268px; text-align: center; font-size: 21px; }
  .recipient {
    position: absolute; left: 0; width: 780px; top: 303px; text-align: center;
    font-family: "Kaushan Script", cursive; font-size: 26px; color: var(--forest);
  }
  .recipient-rule { position: absolute; left: 236px; width: 308px; top: 350px; height: 1px; background: var(--grey-rule); }
  .achievement { position: absolute; left: 0; width: 780px; top: 360px; text-align: center; font-size: 11px; line-height: 15px; }
  .achievement strong { font-weight: 800; }

  .field { position: absolute; width: 134px; text-align: center; font-size: 12px; }
  .field .value { height: 20px; line-height: 20px; }
  .field .rule { height: 1px; background: var(--grey-rule); margin: 2px 0 4px; }
  .field.date { left: 148px; top: 436px; }
  .field.signature { left: 482px; top: 430px; }
  .signature .value { font-family: "Mrs Saint Delafield", cursive; font-size: 26px; height: 26px; line-height: 26px; }

  .seal { position: absolute; left: 354px; top: 425px; }
</style>
</head>
<body>
  <section class="certificate" aria-label="Certificate of completion">
    <div class="ornament-band" role="img" aria-label="Decorative green ornamental border"></div>
    <div class="paper" role="img" aria-label="Soft guilloche line background"></div>

    <div class="content">
      <div class="brand"><span class="brand-dot"></span>Halvorcrest</div>
      <div class="brand-divider"></div>
      <div class="sponsor-info">
        48 Linden Parkway, Ste. 310 Marbury, OR 97402<br>
        <span class="registry">National Registry Sponsor Number 70318</span>
      </div>

      <h1 class="title">Certificate</h1>

      <div class="subtitle-row">
        <span class="rule left"></span><span class="cap left"></span>
        <span class="pill">Of completion</span>
        <span class="cap right"></span><span class="rule right"></span>
      </div>

      <p class="awarded">This Certificate is Awarded</p>
      <p class="recipient">Marcus Elderhollow</p>
      <div class="recipient-rule"></div>

      <p class="achievement">
        <strong>For successful completion of Best Practices:</strong><br>
        Budget Process/Budget Building Completed Online Field of Study<br>
        Finance CPE Credits: 1
      </p>

      <div class="field date">
        <div class="value">23/03/25</div>
        <div class="rule"></div>
        <div>Completion Date</div>
      </div>

      <svg class="seal" width="72" height="72" viewBox="0 0 72 72" role="img" aria-label="Company seal">
        <circle cx="36" cy="36" r="34" fill="var(--forest)"/>
        <circle cx="36" cy="36" r="26" fill="none" stroke="var(--leaf-light)" stroke-width="1"/>
      </svg>

      <div class="field signature">
        <div class="value">Clara Wendell</div>
        <div class="rule"></div>
        <div>Senior Consultant</div>
      </div>
    </div>
  </section>
</body>
</html>
```